Business card design for Automotive workshop

We need a business card for a new automotive repair and tyre shop called Ridgeback Prime Automotive located in New Zealand. We are a clean, modern and fresh workshop and company.

Front needs to feature logo,
my name:
Lachie Westergaard (director)

Address:
48 Marlow Lane
Kowhai Bay 3582

Phone: 07 842 1937
Mobile: 027 519 2764
Email: office@ridgebackmotors.co.nz
Website: ridgebackmotors.co.nz

Back needs to feature an area to write down appointment details, date and time.

Also feature a list of jobs and work we do such as,
Vehicle Servicing
All Mechanical Repairs
Warrant of Fitness
Tyres & Wheel Alignments
Automotive Diagnostics
Automotive Parts & Supplies

```html
<!DOCTYPE html>
<html lang="en">
<head>
<meta charset="utf-8">
<title>Ridgeback Prime Automotive – Business Card</title>
<link rel="stylesheet" href="https://fonts.googleapis.com/css2?family=Alfa+Slab+One&family=Montserrat:wght@400;700;800&display=swap">
<style>
  :root {
    --red: #e21f26;
    --black: #000000;
    --white: #ffffff;
    --ink: #111111;
    --text-font: "Montserrat", sans-serif;
    --label-font: "Alfa Slab One", serif;
  }
  * { margin: 0; padding: 0; box-sizing: border-box; }
  html, body { width: 874px; height: 1200px; overflow: hidden; background: var(--white); }
  .sheet { position: relative; width: 874px; height: 1200px; font-family: var(--text-font); font-variant: small-caps; }
  .side-label {
    position: absolute; left: 0; width: 100%; text-align: center;
    font-family: var(--label-font); font-variant: normal; font-size: 42px; line-height: 1; color: var(--ink);
  }
  .side-label.back { top: 39px; }
  .side-label.front { top: 640px; }

  /* Back */
  .services-band { position: absolute; left: 0; top: 100px; width: 874px; height: 282px; background: var(--red); }
  .services {
    position: absolute; left: 52px; top: 30px; list-style: none;
    color: var(--white); font-size: 36px; line-height: 41.5px; letter-spacing: 0.2px;
  }
  .logo-box {
    position: absolute; left: 504px; top: 31px; width: 335px; height: 118px; background: var(--white);
    display: flex; align-items: center; justify-content: center; text-align: center;
  }
  .logo-box .brand { color: var(--red); font-weight: 800; font-size: 30px; line-height: 30px; }
  .appointment-bar {
    position: absolute; left: 0; top: 388px; width: 874px; height: 47px; background: var(--black);
    color: var(--red); font-weight: 800; font-size: 42px; line-height: 44px; text-align: center;
  }
  .appointment-rule { position: absolute; left: 0; top: 441px; width: 874px; height: 7px; background: var(--red); }
  .appointment-fields { position: absolute; left: 120px; top: 453px; color: var(--ink); font-size: 36px; line-height: 42px; }
  .back-foot { position: absolute; left: 0; top: 533px; width: 874px; height: 49px; background: var(--black); }

  /* Front */
  .front-card { position: absolute; left: 0; top: 698px; width: 874px; height: 502px; background: var(--black); }
  .front-brand {
    position: absolute; left: 0; top: 64px; width: 100%; text-align: center;
    color: var(--red); font-weight: 800; font-size: 62px; line-height: 56px; letter-spacing: 1px;
  }
  .name-band {
    position: absolute; left: 0; top: 191px; width: 874px; height: 97px; background: var(--red);
    text-align: center; color: var(--black); font-weight: 800; font-size: 38px; line-height: 48px; padding-top: 1px;
  }
  .address, .phones { position: absolute; color: var(--white); line-height: 41px; text-align: center; }
  .address { left: 28px; width: 340px; top: 296px; font-size: 37px; font-style: normal; }
  .phones { left: 420px; width: 434px; top: 292px; font-size: 38px; }
  .web { position: absolute; left: 0; width: 100%; text-align: center; color: var(--red); font-size: 42px; line-height: 44px; letter-spacing: 0.5px; }
  .web.email { top: 384px; }
  .web.site { top: 429px; }
</style>
</head>
<body>
<main class="sheet">
  <h2 class="side-label back">Back</h2>

  <section class="services-band">
    <ul class="services">
      <li>Vehicle Servicing</li>
      <li>All Mechanical Repairs</li>
      <li>Warrant of Fitness</li>
      <li>Tyres &amp; Wheel Alignments</li>
      <li>Automotive Diagnostics</li>
      <li>Automotive Parts &amp; Supplies</li>
    </ul>
    <div class="logo-box"><span class="brand">Ridgeback Prime<br>Automotive</span></div>
  </section>
  <div class="appointment-bar">Appointment</div>
  <div class="appointment-rule"></div>
  <div class="appointment-fields">
    <p>Date:</p>
    <p>Time:</p>
  </div>
  <div class="back-foot"></div>

  <h2 class="side-label front">Front</h2>

  <section class="front-card">
    <div class="front-brand">Ridgeback Prime<br>Automotive</div>
    <div class="name-band">
      <p>Lachie Westergaard</p>
      <p>Director</p>
    </div>
    <address class="address">
      <p>48 Marlow Lane</p>
      <p>Kowhai Bay 3582</p>
    </address>
    <div class="phones">
      <p>Phone: 07 842 1937</p>
      <p>Mobile: 027 519 2764</p>
    </div>
    <p class="web email">office@ridgebackmotors.co.nz</p>
    <p class="web site">ridgebackmotors.co.nz</p>
  </section>
</main>
</body>
</html>
```